Roll label Flyer design

I need a flyer for a roll label printer
Pictures for the project are located here:
https://brindlework.filedrop.example/d-k7mx2291q0a553714

Text I want is located here:
https://brindlework.example/roll-labels.php

Target Market(s)

Manufactures, wholesalers

Industry/Entity Type

Printing

Requirements
Must have
• Lots of pictures. Our phone number 800-472-6018. Website www.brindlework.example

```html
<!DOCTYPE html>
<html lang="en">
<head>
<meta charset="utf-8">
<title>Brindlework – Roll/Product Labels Flyer</title>
<link href="https://fonts.googleapis.com/css2?family=Lato:wght@400;700&display=swap" rel="stylesheet">
<style>
  :root {
    --bg: #dfe1e6;
    --ink-dark: #262527;
    --ink-black: #151516;
    --brand-red: #cf2a32;
    --band-grey: #cfcfd1;
    --text-light: #ffffff;
    --text-dark: #2a2a2c;
    --gap: #ffffff;
    --photo-steel: #8f959b;
    --photo-light: #c9cbcd;
    --photo-dark: #3a3c40;
  }
  * { box-sizing: border-box; margin: 0; padding: 0; }
  html, body { width: 1200px; height: 800px; overflow: hidden; background: var(--bg); font-family: "Lato", sans-serif; }

  .flyer {
    position: absolute; left: 330px; top: 20px;
    width: 540px; height: 760px;
    background: var(--gap); overflow: hidden;
    box-shadow: 0 6px 18px rgba(0,0,0,.18);
  }
  .header {
    position: absolute; left: 0; top: 0; width: 100%; height: 78px;
    background: linear-gradient(135deg, #2a2b2e, var(--ink-black));
  }
  .brand {
    position: absolute; left: 26px; top: 22px;
    display: flex; align-items: center; gap: 10px;
    color: var(--text-light); font-weight: 700; font-size: 15px; letter-spacing: 4px; text-transform: uppercase;
  }
  .brand-mark { width: 26px; height: 26px; border-radius: 50%; background: var(--brand-red); }

  .intro {
    position: absolute; left: 0; top: 60px; width: 300px; height: 108px;
    background: var(--brand-red); color: var(--text-light);
    padding: 16px 20px; font-size: 11.5px; line-height: 1.4;
  }
  .title-box {
    position: absolute; right: 14px; top: 96px; width: 250px; height: 56px;
    background: var(--ink-black); border: 1.5px solid var(--text-light);
    color: var(--text-light); padding: 7px 12px; text-align: right;
  }
  .title-box h1 { font-size: 21px; font-weight: 700; line-height: 1.1; white-space: nowrap; }
  .title-box p { font-size: 8px; letter-spacing: .3px; text-transform: uppercase; margin-top: 4px; white-space: nowrap; }

  .photo { position: absolute; }
  .p-1 { left: 300px; top: 168px; width: 240px; height: 150px; background: linear-gradient(160deg, var(--photo-light), var(--photo-dark)); }
  .p-2 { left: 0; top: 172px; width: 296px; height: 150px; background: linear-gradient(120deg, var(--photo-light), var(--photo-steel)); }
  .p-3 { left: 0; top: 326px; width: 110px; height: 210px; background: linear-gradient(180deg, var(--photo-steel), var(--photo-dark)); }
  .p-4 { left: 254px; top: 322px; width: 140px; height: 120px; background: linear-gradient(150deg, var(--photo-dark), #6b6e72); }
  .p-5 { left: 398px; top: 322px; width: 142px; height: 150px; background: linear-gradient(150deg, var(--photo-steel), #b9a0a3); }
  .p-6 { left: 254px; top: 446px; width: 140px; height: 130px; background: linear-gradient(170deg, var(--photo-light), var(--photo-steel)); }
  .p-7 { left: 398px; top: 476px; width: 142px; height: 100px; background: linear-gradient(170deg, #e6e6e6, var(--photo-steel)); }

  .features {
    position: absolute; left: 22px; top: 356px; width: 226px; height: 176px;
    background: var(--brand-red); color: var(--text-light); padding: 14px 18px;
  }
  .features h2 { font-size: 17px; font-weight: 400; margin-bottom: 6px; }

  .check-list { list-style: none; font-size: 11px; line-height: 1.45; }
  .check-list li { display: flex; gap: 6px; align-items: baseline; }
  .check-list svg { flex: none; width: 10px; height: 10px; align-self: flex-start; margin-top: 3px; }

  .markets {
    position: absolute; left: 0; top: 580px; width: 100%; height: 122px;
    background: var(--band-grey); color: var(--text-dark); padding: 16px 26px;
  }
  .markets h2 { font-size: 18px; font-weight: 400; margin-bottom: 8px; }
  .markets-cols { display: flex; gap: 36px; }
  .markets .check-list { font-size: 11.5px; }
  .small { font-size: 8px; margin-left: 4px; }

  .footer {
    position: absolute; left: 0; bottom: 0; width: 100%; height: 58px;
    background: var(--ink-dark); color: var(--text-light);
    display: flex; align-items: center; justify-content: center; gap: 48px; font-size: 14px;
  }
  .footer span { display: flex; align-items: center; gap: 8px; }
  .footer svg { width: 15px; height: 15px; }
</style>
</head>
<body>
<main class="flyer">
  <header class="header">
    <div class="brand"><span class="brand-mark"></span>Brindlework</div>
  </header>

  <div class="photo p-1" role="img" aria-label="Operator working among roll label presses in a print plant"></div>
  <div class="photo p-2" role="img" aria-label="Close-up of a label press with rollers and label webs"></div>
  <div class="photo p-3" role="img" aria-label="Rolls of printed product labels"></div>
  <div class="photo p-4" role="img" aria-label="Label roll unwinding on a press"></div>
  <div class="photo p-5" role="img" aria-label="Printed red labels on a finishing line"></div>
  <div class="photo p-6" role="img" aria-label="Printed labels on a conveyor"></div>
  <div class="photo p-7" role="img" aria-label="Rewinding unit of a label press"></div>

  <div class="intro">Long or short run. Digital or flexographic. Standard shapes or unique, custom diecuts. Simple spot colors or full color with every embellishment. Let us help you create the perfect label for your application.</div>

  <div class="title-box">
    <h1>Roll/Product Labels</h1>
    <p>Foil-Stamping, Embossing, Spot Varnishing</p>
  </div>

  <section class="features">
    <h2>Features:</h2>
    <ul class="check-list">
      <li><svg viewBox="0 0 10 10"><path d="M1 5l3 3 5-7" fill="none" stroke="currentColor" stroke-width="1.6"/></svg>Foil-Stamping</li>
      <li><svg viewBox="0 0 10 10"><path d="M1 5l3 3 5-7" fill="none" stroke="currentColor" stroke-width="1.6"/></svg>Embossing</li>
      <li><svg viewBox="0 0 10 10"><path d="M1 5l3 3 5-7" fill="none" stroke="currentColor" stroke-width="1.6"/></svg>Spot Varnishes</li>
      <li><svg viewBox="0 0 10 10"><path d="M1 5l3 3 5-7" fill="none" stroke="currentColor" stroke-width="1.6"/></svg>Instant Redeemable Coupons</li>
      <li><svg viewBox="0 0 10 10"><path d="M1 5l3 3 5-7" fill="none" stroke="currentColor" stroke-width="1.6"/></svg>Expanded Content/Booklet Labels</li>
    </ul>
  </section>

  <section class="markets">
    <h2>Specialty Markets We Service Include:</h2>
    <div class="markets-cols">
      <ul class="check-list">
        <li><svg viewBox="0 0 10 10"><path d="M1 5l3 3 5-7" fill="none" stroke="currentColor" stroke-width="1.6"/></svg>Health &amp; Beauty</li>
        <li><svg viewBox="0 0 10 10"><path d="M1 5l3 3 5-7" fill="none" stroke="currentColor" stroke-width="1.6"/></svg>Food &amp; Beverage</li>
        <li><svg viewBox="0 0 10 10"><path d="M1 5l3 3 5-7" fill="none" stroke="currentColor" stroke-width="1.6"/></svg>Wine &amp; Spirits</li>
      </ul>
      <ul class="check-list">
        <li><svg viewBox="0 0 10 10"><path d="M1 5l3 3 5-7" fill="none" stroke="currentColor" stroke-width="1.6"/></svg>Industrial Safety &amp; Warning</li>
        <li><svg viewBox="0 0 10 10"><path d="M1 5l3 3 5-7" fill="none" stroke="currentColor" stroke-width="1.6"/></svg>Promotional</li>
        <li><svg viewBox="0 0 10 10"><path d="M1 5l3 3 5-7" fill="none" stroke="currentColor" stroke-width="1.6"/></svg>Compliance<span class="small">(I.E. NSL, QTA, Westland Rule 12)</span></li>
      </ul>
    </div>
  </section>

  <footer class="footer">
    <span>
      <svg viewBox="0 0 16 16"><path d="M4 1h3l1 4-2 1.5c.8 2 2 3.2 3.5 3.5L11 8l4 1v3c0 1-1 2-2 2C7 14 2 9 2 3c0-1 1-2 2-2z" fill="currentColor"/></svg>
      800-472-6018
    </span>
    <span>
      <svg viewBox="0 0 16 16" fill="none" stroke="currentColor" stroke-width="1.2"><circle cx="8" cy="8" r="6.5"/><ellipse cx="8" cy="8" rx="3" ry="6.5"/><path d="M1.5 8h13M2.5 4.5h11M2.5 11.5h11"/></svg>
      www.brindlework.example
    </span>
  </footer>
</main>
</body>
</html>
```